Everything fresh, everything new

When I take over the practice, I would like to breathe new life into the practice. I want a business card design that catches the eye and brings a breath of fresh air

```html
<!DOCTYPE html>
<html lang="de">
<head>
<meta charset="utf-8">
<title>Bewegungsraum – Visitenkarte</title>
<link rel="stylesheet" href="https://fonts.googleapis.com/css2?family=Montserrat:wght@400;500;600;700&display=swap">
<style>
  :root {
    --page: #e9eaec;
    --card-dark: #575757;
    --card-light: #ffffff;
    --green: #8cc63f;
    --ink: #3a3a3a;
    --ink-soft: #7a7a7a;
    --on-dark: #2b2b2b;
  }
  * { box-sizing: border-box; margin: 0; padding: 0; }
  html, body { width: 900px; height: 1200px; overflow: hidden; }
  body {
    background: var(--page);
    font-family: "Montserrat", Arial, sans-serif;
    position: relative;
  }
  .card {
    position: absolute;
    left: 70px;
    width: 760px;
    height: 490px;
    box-shadow: 0 10px 30px rgba(0,0,0,0.18);
  }
  .card--front { top: 90px; background: var(--card-dark); }
  .card--back { top: 620px; background: var(--card-light); }

  .brand {
    position: absolute;
    left: 0; right: 0;
    display: flex;
    flex-direction: column;
    align-items: center;
  }
  .brand__row { display: flex; align-items: center; gap: 18px; }
  .brand__dot {
    width: 30px; height: 30px;
    border-radius: 50%;
    background: var(--green);
  }
  .brand__name {
    font-weight: 600;
    font-size: 58px;
    letter-spacing: -1px;
  }
  .brand__tagline {
    margin-top: 10px;
    font-size: 17px;
    font-weight: 500;
    color: var(--green);
    letter-spacing: 0.5px;
  }
  .card--front .brand { top: 190px; }
  .card--front .brand__name { color: var(--on-dark); }
  .card--back .brand { top: 70px; }
  .card--back .brand__name { color: var(--ink); font-size: 50px; }
  .card--back .brand__tagline { font-size: 15px; }

  .person {
    position: absolute;
    left: 80px;
    top: 300px;
    width: 260px;
    text-align: right;
  }
  .person__name { font-size: 30px; font-weight: 700; color: var(--green); }
  .person__role { margin-top: 6px; font-size: 15px; color: var(--ink-soft); letter-spacing: 1px; }

  .divider {
    position: absolute;
    left: 366px;
    top: 295px;
    width: 3px;
    height: 120px;
    background: var(--green);
  }
  .contact {
    position: absolute;
    left: 392px;
    top: 296px;
    list-style: none;
  }
  .contact__item {
    display: flex;
    align-items: center;
    gap: 14px;
    height: 40px;
    font-size: 18px;
    color: var(--ink);
  }
  .contact__icon { width: 20px; height: 20px; flex: none; }
</style>
</head>
<body>
  <section class="card card--front">
    <div class="brand">
      <div class="brand__row">
        <span class="brand__name">Bewegungsraum</span>
        <span class="brand__dot"></span>
      </div>
      <p class="brand__tagline">Praxis für Physiotherapie</p>
    </div>
  </section>

  <section class="card card--back">
    <div class="brand">
      <div class="brand__row">
        <span class="brand__name">Bewegungsraum</span>
        <span class="brand__dot"></span>
      </div>
      <p class="brand__tagline">Praxis für Physiotherapie</p>
    </div>

    <div class="person">
      <p class="person__name">Lukas Moreno</p>
      <p class="person__role">CEO</p>
    </div>

    <div class="divider"></div>

    <ul class="contact">
      <li class="contact__item">
        <svg class="contact__icon" viewBox="0 0 24 24"><path fill="#8cc63f" d="M6.6 10.8a15.1 15.1 0 0 0 6.6 6.6l2.2-2.2c.3-.3.7-.4 1-.2 1.1.4 2.3.6 3.6.6.6 0 1 .4 1 1V20c0 .6-.4 1-1 1A17 17 0 0 1 3 4c0-.6.4-1 1-1h3.5c.6 0 1 .4 1 1 0 1.3.2 2.5.6 3.6.1.3 0 .7-.2 1z"/></svg>
        <span>+34 910 482 317</span>
      </li>
      <li class="contact__item">
        <svg class="contact__icon" viewBox="0 0 24 24"><rect x="2" y="5" width="20" height="14" rx="2" fill="#8cc63f"/><path d="M3 6l9 7 9-7" fill="none" stroke="#fff" stroke-width="1.6"/></svg>
        <span>lukas@bewegungsraum.com</span>
      </li>
      <li class="contact__item">
        <svg class="contact__icon" viewBox="0 0 24 24"><circle cx="12" cy="12" r="10" fill="#8cc63f"/><path d="M2 12h20M12 2c3 3 3 17 0 20M12 2c-3 3-3 17 0 20" fill="none" stroke="#fff" stroke-width="1.3"/></svg>
        <span>www.bewegungsraum.com</span>
      </li>
    </ul>
  </section>
</body>
</html>
```